Online trading school - Website design

We are building an online trading school (trading of shares, commodities, indices, currencies). The purpose is to teach online traders how to trade successfully. We need to design the homepage of the website and logo (bramwelloq.com will be the domain). The homepage will contain the following elements

- logo
- Sign in and Register links/buttons
- upper menu
- short introduction
- a couple of bullet points 'Why to join our school?'
- sign up form
- text
- bottom menu

Attached is a draft for the designer. The draft is just for an inspiration, the actual structure of the website can be different if the designer thinks so.

The designer is free to choose colors.

School

3 page

```html
<!DOCTYPE html>
<html lang="en">
<head>
<meta charset="utf-8">
<title>Bramwelloq – Online Trading School</title>
<link rel="stylesheet" href="https://fonts.googleapis.com/css2?family=Arimo:wght@400;700&family=Hind:wght@400;500;600&display=swap">
<style>
:root{
  --blue:#17479c;
  --orange:#e05a04;
  --dark:#222222;
  --footer:#3a3a3a;
  --white:#ffffff;
  --text:#2e2e2e;
}
*{margin:0;padding:0;box-sizing:border-box}
html,body{width:1200px;height:1098px;overflow:hidden;background:var(--white)}
body{position:relative;font-family:"Arimo",Arial,sans-serif;color:var(--text)}
.abs{position:absolute}

.site-header{left:0;top:0;width:1200px;height:86px;background:var(--white)}
.brand{left:60px;top:22px;display:flex;align-items:center;gap:10px;font-family:"Arimo",Arial,sans-serif;font-size:35px;color:var(--dark)}
.brand-dot{width:34px;height:34px;border-radius:50%;background:var(--blue)}
.social{top:32px;width:27px;height:27px;border:1.5px solid #333;border-radius:50%}
.btn{top:26px;height:37px;display:flex;align-items:center;justify-content:center;font-family:"Hind",sans-serif;font-size:19px;color:var(--white);border-radius:2px}
.btn-signin{left:934px;width:94px;background:var(--orange)}
.btn-register{left:1039px;width:99px;background:var(--dark)}

.main-nav{left:0;top:86px;width:1200px;height:42px;background:var(--blue)}
.nav-item{top:12px;font-family:"Hind",sans-serif;font-weight:600;font-size:14.5px;color:var(--white);letter-spacing:.1px}
.nav-item.active{border-bottom:2px solid var(--orange);padding-bottom:5px}

.hero-photo{left:0;top:128px;width:1200px;height:312px;background:linear-gradient(100deg,#3b3632 0%,#5a554f 35%,#47413c 65%,#3a3430 100%)}
.hero-title{left:0;top:200px;width:1200px;text-align:center;color:var(--white);font-size:21px;line-height:30px;text-transform:uppercase;letter-spacing:.2px}

.port-photo{left:0;top:440px;width:1200px;height:608px;background:linear-gradient(180deg,#eef0f3 0%,#e7e4e3 40%,#ecdcd8 70%,#ddd6d6 100%)}

.why-panel{left:60px;top:335px;width:541px;height:357px;background:var(--orange)}
.why-title{left:42px;top:50px;font-size:29px;font-weight:700;color:var(--white);letter-spacing:.5px}
.why-list{left:42px;top:108px;list-style:none}
.why-list li{display:flex;align-items:center;gap:12px;height:39.7px;font-family:"Hind",sans-serif;font-weight:500;font-size:20px;color:var(--white)}
.bullet{width:15px;height:15px;border-radius:50%;background:var(--white);border:4px solid var(--blue);flex:none}

.join-panel{left:601px;top:335px;width:539px;height:357px;background:var(--blue)}
.join-title{right:56px;top:48px;font-size:29px;font-weight:700;color:var(--white);letter-spacing:.5px}
.field{left:131px;width:353px;height:40px;background:var(--white);padding-left:13px;display:flex;align-items:center;font-size:15px;color:#777}
.agree{left:131px;top:272px;display:flex;align-items:center;gap:8px;font-size:13.5px;color:var(--white)}
.check{width:15px;height:15px;background:#f2f2f2;border:1px solid #bbb}
.submit{left:388px;top:270px;width:96px;height:39px;background:var(--orange);color:var(--white);font-weight:700;font-size:15px;display:flex;align-items:center;justify-content:center}

.emblem{left:550px;top:462px;width:108px;height:108px;border-radius:50%;background:var(--white)}

.offer-title{left:0;top:766px;width:1294px;text-align:center;font-size:35px;font-weight:700;color:var(--dark);letter-spacing:1.5px}
.offer-rule{left:558px;top:820px;width:111px;height:3px;background:var(--blue)}
.offer-text{left:115px;top:852px;width:962px;text-align:center;font-size:15.5px;line-height:22.2px;color:#333}
.offer-text p+p{margin-top:22px}

.site-footer{left:0;top:1048px;width:1200px;height:50px;background:var(--footer);color:var(--white);font-size:16px}
.copyright{left:63px;top:15px}
.footer-links{right:60px;top:15px}
</style>
</head>
<body>

<header class="abs site-header">
  <div class="abs brand"><span class="brand-dot"></span>Bramwelloq</div>
  <span class="abs social" style="left:779px"></span>
  <span class="abs social" style="left:816px"></span>
  <span class="abs social" style="left:853px"></span>
  <span class="abs social" style="left:890px"></span>
  <a class="abs btn btn-signin">Sign in</a>
  <a class="abs btn btn-register">Register</a>
</header>

<nav class="abs main-nav">
  <span class="abs nav-item active" style="left:63px">ABOUT OUR SCHOOL</span>
  <span class="abs nav-item" style="left:250px">RISK WARNING</span>
  <span class="abs nav-item" style="left:391px">FAQ</span>
  <span class="abs nav-item" style="left:462px">TRADING GLOSSARY</span>
  <span class="abs nav-item" style="left:642px">CONTACT</span>
</nav>

<div class="abs hero-photo" role="img" aria-label="Photo of students attending a trading seminar, darkened"></div>
<h1 class="abs hero-title" style="font-weight:400">An online digital trading course that will walk you through the simple<br>process of extracting cash from the market</h1>

<div class="abs port-photo" role="img" aria-label="Faded photo of a container ship and cranes at a cargo port"></div>

<section class="abs why-panel">
  <h2 class="abs why-title">WHY TO JOIN US?</h2>
  <ul class="abs why-list">
    <li><span class="bullet"></span>Best trading tips ever</li>
    <li><span class="bullet"></span>Secret tips from experts</li>
    <li><span class="bullet"></span>We teach you how to trade online</li>
    <li><span class="bullet"></span>Learn how to trade commodities</li>
    <li><span class="bullet"></span>Learn How to become a trader</li>
  </ul>
</section>

<section class="abs join-panel">
  <h2 class="abs join-title">JOIN OUR SCHOOL NOW!</h2>
  <div class="abs field" style="top:105px">First name</div>
  <div class="abs field" style="top:159px">Last name</div>
  <div class="abs field" style="top:211px">Email</div>
  <div class="abs agree"><span class="check"></span>Agree with our terms and conditions</div>
  <div class="abs submit">SUBMIT</div>
</section>

<div class="abs emblem"></div>

<h2 class="abs offer-title">WHAT DO WE OFFER?</h2>
<div class="abs offer-rule"></div>
<div class="abs offer-text">
  <p>Lorem Ipsum is simply dummy text of the printing and typesetting industry. Lorem Ipsum has been the industry's standard dummy text ever since the 1500s, when an unknown printer took a galley of type and scrambled it to make a type specimen book. It has survived not only five centuries, but also the leap into electronic typesetting, remaining essentially unchanged.</p>
  <p>It was popularised in the 1960s with the release of Lettrafold sheets containing Lorem Ipsum passages, and more recently with desktop publishing software like Alden PageForge including versions of Lorem Ipsum.</p>
</div>

<footer class="abs site-footer">
  <span class="abs copyright">Copyright © Bramwelloq.com. All Rights Reserved.</span>
  <span class="abs footer-links">Terms &amp; Conditions &nbsp;|&nbsp; Privacy Policy</span>
</footer>

</body>
</html>
```